Design home page for brightvane.xyz

We’re seeking a sleek, lead-generation-focused single-page website for Brightvane.xyz that communicates our expertise in delivering high-intent leads to mid-sized businesses. The goal is to guide visitors toward scheduling a free consultation while emphasizing our performance-based approach and comprehensive service offerings.

Industry/Entity Type

Marketing

Number of Pages Required

1 page

Font styles to use
Sans Serif

Requirements
Must have
• content from https://files.quorvalet.example/doc/7hTmwQRZa93KpLdVyxNe42UcBsFoGj8rYiMn5EkPtWz/view?tab=t.0
Nice to have
• color pallet from here https://files.quorvalet.example/doc/4pRkz-NWb62VxLeTyqJs8cHaDmFu3GiYoBnQ5tXeKv/view?tab=t.0

```html
<!DOCTYPE html>
<html lang="en">
<head>
<meta charset="utf-8">
<title>Brightvane.xyz — High-Intent Lead Generation</title>
<link href="https://fonts.googleapis.com/css2?family=Montserrat:wght@700;800&family=Figtree:wght@400;500;600;700&display=swap" rel="stylesheet">
<style>
:root{
  --cream:#fdf8ee;
  --grid:#f2e9d3;
  --red:#a3121b;
  --orange:#f5a21a;
  --ink:#1f1f1f;
  --text:#3a3a3a;
  --dark:#333333;
  --slate:#6b727c;
  --white:#ffffff;
}
*{box-sizing:border-box;margin:0;padding:0}
html,body{width:1200px;height:3213px;overflow:hidden}
body{font-family:"Figtree",sans-serif;color:var(--text);background:var(--cream)}
h1,h2,h3{font-family:"Montserrat",sans-serif;color:var(--ink)}
.grid-bg{background-color:var(--cream);
  background-image:linear-gradient(var(--grid) 1px,transparent 1px),linear-gradient(90deg,var(--grid) 1px,transparent 1px);
  background-size:30px 30px}
.section{position:relative;width:1200px}
.center-title{text-align:center;font-size:31px;line-height:37px;font-weight:700}
.hl{position:relative;display:inline-block}
.hl::after{content:"";position:absolute;left:0;right:0;bottom:-2px;height:4px;border-radius:3px;background:var(--orange)}
.red-bar{width:44px;height:3px;background:var(--red);margin:10px auto 0}
.lead{text-align:center;font-size:15px;line-height:22px;color:var(--ink)}

/* content formats */
.formats{height:1125px}
.formats .center-title{padding-top:60px}
.formats .lead{margin-top:28px}
.tags{width:860px;margin:22px auto 0;display:flex;flex-wrap:wrap;justify-content:center;gap:12px 10px}
.tag{background:var(--red);color:var(--white);font-size:14.5px;height:32px;line-height:32px;padding:0 10px;border-radius:16px}
.divider{position:absolute;left:161px;width:878px;height:16px;display:flex;align-items:center;gap:18px}
.divider .rule{flex:1;height:1px;background:#d68a8f}
.divider .dots{display:flex;gap:9px}
.divider .dots i{width:4px;height:4px;border-radius:50%;background:var(--ink)}
.process-title{position:absolute;top:464px;left:0;right:0}
.process-lead{position:absolute;top:578px;left:0;right:0}
.cards{position:absolute;top:665px;left:161px;display:flex;gap:19px;align-items:flex-start}
.card{width:280px;background:var(--white);border-radius:8px;padding:32px 28px 28px 29px}
.icon{width:45px;height:45px;border:2px solid var(--orange);border-radius:50%;display:flex;align-items:center;justify-content:center}
.card h3{font-family:"Figtree",sans-serif;font-size:17px;line-height:26px;font-weight:700;margin-top:12px;width:200px}
.card p{font-size:14.5px;line-height:22.5px;margin-top:10px;color:var(--text)}

/* dark band */
.apart{height:767px;background:var(--dark);color:var(--white)}
.col{position:absolute;top:0;width:374px}
.col h2{color:var(--white);font-size:28px;line-height:37px;font-weight:800}
.col .obar{width:44px;height:3px;background:var(--orange);margin-top:22px}
.col .intro{font-size:15px;line-height:22.5px;margin-top:30px;color:#f1f1f1}
.box{background:var(--slate);border-radius:6px;padding:16px 21px 16px;margin-top:18px}
.box h3{font-family:"Figtree",sans-serif;color:var(--white);font-size:16.5px;font-weight:700;padding-bottom:10px;border-bottom:1px solid #c0303a}
.box p{font-size:14.5px;line-height:22.5px;margin-top:10px;color:#f3f3f3}

/* testimonials */
.stories{height:1046px}
.stories .center-title{padding-top:78px}
.stories .lead{margin-top:28px}
.stories .lead b{color:var(--red);font-weight:700}
.quotes{position:absolute;top:2123px;top:231px;left:161px;display:flex;gap:19px}
.quote{width:280px;height:328px;background:var(--white);border-radius:8px;padding:22px 20px 0 20px}
.avatar{width:45px;height:45px;border:1.5px solid var(--red);border-radius:50%}
.qmark{color:var(--orange);font-family:"Montserrat",sans-serif;font-weight:800;font-size:20px;line-height:20px;margin-top:12px;font-style:italic}
.quote p{font-size:14.5px;line-height:22.5px;margin-top:6px;color:var(--text)}
.who{border-left:1.5px solid var(--orange);padding-left:14px;margin-top:14px;font-size:12.5px;line-height:15px;color:var(--ink)}
.who b{display:block;color:var(--red);font-weight:700;margin-bottom:2px}
.cta{position:absolute;top:605px;left:161px;width:878px;height:374px;background:var(--dark);border-radius:6px;color:var(--white)}
.cta h2{position:absolute;left:35px;top:34px;color:var(--white);font-size:29px;line-height:37px;font-weight:800}
.cta .body{position:absolute;left:35px;top:130px;width:400px;font-size:14.5px;line-height:22.5px}
.cta ul{list-style:none;margin-top:20px}
.cta li{position:relative;padding-left:15px}
.cta li::before{content:"•";position:absolute;left:0;color:var(--orange)}
.cta li b{font-weight:700}
.art{position:absolute;left:540px;top:35px;width:250px;height:245px;border-radius:8px;background:radial-gradient(circle at 50% 45%,#f6f1ea 0%,#c9b39b 45%,#3a3a3a 75%)}
.btn{position:absolute;left:546px;top:292px;width:220px;height:44px;background:var(--red);color:var(--white);font-size:15px;font-weight:600;text-align:center;line-height:44px;border-radius:6px}

/* footer */
.footer{height:275px;background:var(--dark);text-align:center;color:var(--white)}
.logo{padding-top:53px;font-family:"Figtree",sans-serif;font-size:35px;font-weight:700;line-height:44px}
.tagline{font-size:16px;font-weight:600;margin-top:6px}
.footer .obar{width:44px;height:3px;background:var(--orange);margin:20px auto 0}
.copy{font-size:14.5px;margin-top:24px}
</style>
</head>
<body>

<section class="section formats grid-bg">
  <h1 class="center-title"><span class="hl">Tailored Content</span> for<br>High-Intent Lead Capture</h1>
  <div class="red-bar"></div>
  <p class="lead">We create custom-crafted content tailored for your audience.</p>
  <div class="tags">
    <span class="tag">· Guides and eBooks</span>
    <span class="tag">· Industry Insights Reports</span>
    <span class="tag">· Infographics &amp; Visual Guides</span>
    <span class="tag">· Glossary of Industry Terms</span>
    <span class="tag">· Checklist for Best Practices</span>
    <span class="tag">· Trend Spotting Forecast</span>
    <span class="tag">· Templates and Toolkits</span>
    <span class="tag">· Competitive Landscape</span>
    <span class="tag">· Whitepapers</span>
  </div>

  <div class="divider" style="top:396px"><span class="rule"></span><span class="dots"><i></i><i></i><i></i></span></div>

  <h2 class="center-title process-title">How We Deliver<br><span class="hl">High-Quality</span> Leads<div class="red-bar"></div></h2>
  <p class="lead process-lead">Our streamlined process ensures you receive ready-to-engage<br>leads without the hassle.</p>

  <div class="cards">
    <div class="card">
      <div class="icon"><svg width="20" height="20" viewBox="0 0 20 20" fill="none" stroke="#a3121b" stroke-width="1.8"><circle cx="10" cy="10" r="6"/><circle cx="10" cy="10" r="2"/><path d="M10 1v3M10 16v3M1 10h3M16 10h3"/></svg></div>
      <h3>Precise Market Targeting</h3>
      <p>We start by understanding your ideal customer profile and identifying high-intent prospects in your market.</p>
    </div>
    <div class="card">
      <div class="icon"><svg width="22" height="20" viewBox="0 0 22 20" fill="none" stroke="#a3121b" stroke-width="1.8"><circle cx="8" cy="6" r="3.5"/><path d="M2 18c0-4 3-6 6-6"/><circle cx="16" cy="14" r="3"/><path d="M16 9.5v1.5M16 17v1.5M11.5 14H13M19 14h1.5"/></svg></div>
      <h3>Customized Campaign Execution</h3>
      <p>We take the time to understand your audience, creating and running campaigns tailored to their interests, leveraging insights from advertising, SEO, and lead magnets.</p>
    </div>
    <div class="card">
      <div class="icon"><svg width="20" height="20" viewBox="0 0 20 20" fill="none" stroke="#a3121b" stroke-width="1.8"><path d="M2 2l5 5M7 3v4H3M18 2l-5 5M13 3v4h4M2 18l5-5M3 13h4v4M18 18l-5-5M17 13h-4v4"/></svg></div>
      <h3>All-Inclusive Management</h3>
      <p>From strategy to execution, we handle every detail, delivering leads while you focus on closing deals.</p>
    </div>
  </div>

  <div class="divider" style="top:1052px"><span class="dots"><i></i><i></i><i></i></span><span class="rule"></span></div>
</section>

<section class="section apart">
  <div class="col" style="left:193px;top:63px">
    <h2>What Sets Us Apart?</h2>
    <div class="obar"></div>
    <p class="intro">We’re more than just a lead generation service—our approach ensures valuable opportunities for your business.</p>
    <div class="box"><h3>High-Intent Leads</h3><p>The high-intent leads we generate provide a solid starting point for building meaningful connections.</p></div>
    <div class="box"><h3>Complete Service</h3><p>We take care of everything needed to generate leads, so you can stay focused on growing your business.</p></div>
    <div class="box"><h3>Success-Based Partnership</h3><p>With our results-driven model, you pay only for the leads we deliver, ensuring value every step of the way.</p></div>
  </div>
  <div class="col" style="left:632px;top:63px">
    <h2>Comprehensive<br>End-to-End<br>Lead Generation</h2>
    <div class="obar"></div>
    <p class="intro">We simplify lead generation, so you can focus on growing your business.</p>
    <div class="box"><h3>Hands-Off Convenience</h3><p>We manage the strategy, content, advertising, and optimization, delivering a steady flow of high-quality prospects.</p></div>
    <div class="box"><h3>Built to Scale</h3><p>Our process adapts to your growth goals, ensuring consistent lead flow whether you're starting small or scaling rapidly.</p></div>
  </div>
</section>

<section class="section stories grid-bg">
  <h2 class="center-title">Proven <span class="hl">Success Stories</span></h2>
  <div class="red-bar"></div>
  <p class="lead">Discover how our clients have achieved exceptional growth<br>with <b>Brightvane.xyz</b>.</p>

  <div class="quotes">
    <div class="quote">
      <div class="avatar"></div>
      <div class="qmark">“</div>
      <p>Brightvane.xyz has completely transformed our lead generation efforts. We’ve seen a 35% increase in high-quality leads in just three months.</p>
      <div class="who"><b>Reid M.</b>VP of Sales at a Mid-Sized<br>B2B Firm</div>
    </div>
    <div class="quote">
      <div class="avatar"></div>
      <div class="qmark">“</div>
      <p>The team at Brightvane.xyz took care of everything—from content to campaigns. Their performance-based model meant we only paid when results came in. It’s a win-win!</p>
      <div class="who"><b>Priya K.</b>CEO of a Professional Services<br>Company</div>
    </div>
    <div class="quote">
      <div class="avatar"></div>
      <div class="qmark">“</div>
      <p>Working with Brightvane.xyz is like having an in-house growth team. Their ability to create and optimize content-driven campaigns helped us double our inbound inquiries.</p>
      <div class="who"><b>Owen T.</b>Marketing Director at a<br>SaaS Company</div>
    </div>
  </div>

  <div class="cta">
    <h2>Ready to Unlock Scalable<br>Growth for Your Business?</h2>
    <div class="body">
      <p>Schedule a call to learn how we can help your business grow predictably and efficiently.<br>Our proven strategies are tailored to deliver:</p>
      <ul>
        <li><b>High-Intent Leads</b> that match your ideal customer profile.</li>
        <li><b>Custom Campaigns</b> designed to engage and convert your audience.</li>
        <li><b>Actionable Insights</b> to optimize performance and scale effectively.</li>
      </ul>
    </div>
    <div class="art" role="img" aria-label="Illustration of a monitor showing a rising bar chart with a dollar coin and orange and red rings"></div>
    <div class="btn">Schedule Your Call Now</div>
  </div>
</section>

<footer class="section footer">
  <div class="logo">brightvane.xyz</div>
  <div class="tagline">Driving Real Growth, One Lead at a Time</div>
  <div class="obar"></div>
  <div class="copy">Copyright 2025 Brightvane.xyz, LLC. All rights reserved.</div>
</footer>

</body>
</html>
```